HARBOURLINE FORGE GYM FLYER DESIGN

We want a flyer designed for our gym. We have an example of a flyer which we like and I have put it into the images I have uploaded. I would like to recreate using our pictures, so its a pretty straight forward job. We also want to put our weekly timetable on the back of the flyer. We would like the size of the flyer to be A5.

Target Market(s)

FITNESS

Industry/Entity Type

Gym

Colors
33a6d7
ffffff

Requirements
Must have
• We just want to recreate the flyer but we must have the following info on the flyer and we want our timetable on the back of the flyer which you can get from this link: http://www.harbourlineforgegym.com/timetable
• Harbourline Forge Gym is a fun community of humble people. Our goal is to help guide you towards a fitter, healthier lifestyle!
• Our Programs
• HIIT
• High intensity interval training is 30-45 minutes of fat burning fun. The class is a mix of cardio, bodyweight and some resistance movements.
• Conditioning
• A full hour of strength, cardio and bodyweight training to get you in tip top shape. Expect a mix of barbells, kettlebells, rowing machines, bikes and other training methods.
• QMP
• This is our big Friday session to set you up for the weekend. 90 minutes of hard training that is done with a team emphasis. From heavy lifting to cardio triathlons, this class has it all but not for the faint hearted.
• Muay Thai
• Commonly known as the science of 8 limbs you will learn how to punch, kick, knee and elbow. Thailands national sport is a great way to get your fitness kick. We train the complete beginner all the way to international fighters so you are in great hands.
• Kids Muay Thai
• Our junior program starts from age 6 onwards. Muay Thai is a great way for kids to get active and fit while learning new skills. Training in martial arts also teaches self discipline and socialisation skills.
• Yoga
• A combination of physical and mental practises that will leave you focused and refreshed for whatever the week throws at you. We always recommend our yoga classes as a great way to balance the high intensity training we offer.
• Q-Move
• Strength training with a little bit of conditioning. We regularly update the program and re test lifts to ensure you are making progress and getting stronger.
• CONTACT US
• OUR LOCATION:
• Unit 27C
• 214 Caskin Street
• Wester Holm
• Glasgow
• G72LT
• Phone: 07392615084
• Email: info@harbourlineforgegym.com
• Web: www.harbourlineforgegym.com
Nice to have
• Can use all the picture but if not be good to use the boxing one and the group training one.

```html
<!DOCTYPE html>
<html lang="en">
<head>
<meta charset="utf-8">
<title>Harbourline Forge Gym Flyer</title>
<link href="https://fonts.googleapis.com/css2?family=Anton&family=Oswald:wght@500;600&family=Roboto+Condensed:wght@400;700&family=Source+Sans+3:wght@400;600;700&display=swap" rel="stylesheet">
<style>
:root{
  --ink:#111111;
  --paper:#ffffff;
  --stage:#d9d9d9;
  --text-dark:#2b2b2b;
  --grey-bar:#8a8a8a;
  --blue:#5b9bd5;      --blue-t:#d3e3f3;
  --violet:#6f3a96;    --violet-t:#e4d6ee;
  --magenta:#a8409a;   --magenta-t:#eed9ec;
  --amber:#eda23a;     --amber-t:#fbeacd;
  --pink:#cf5aa6;      --pink-t:#f6dfee;
  --black-t:#d2d2d2;
  --orange:#ee7b24;    --orange-t:#fbdfc8;
}
*{margin:0;padding:0;box-sizing:border-box}
html,body{width:1200px;height:897px;overflow:hidden;background:var(--stage)}
.canvas{position:relative;width:1200px;height:897px}

/* Front page */
.front{position:absolute;left:66px;top:77px;width:526px;height:743px;overflow:hidden;background:var(--paper)}
.front-bg{position:absolute;inset:0}
.headline{position:absolute;left:28px;top:28px;width:480px;font-family:"Oswald",sans-serif;font-weight:600;font-size:31px;line-height:34px;color:var(--paper);text-align:center;letter-spacing:.3px}
.tagline{position:absolute;right:28px;top:108px;width:220px;text-align:center;font-family:"Source Sans 3",sans-serif;font-weight:600;font-size:15px;line-height:19px;color:var(--paper)}
.section-title{position:absolute;left:28px;top:176px;font-family:"Source Sans 3",sans-serif;font-weight:600;font-size:30px;color:var(--text-dark);border-bottom:2px solid var(--text-dark);padding-right:2px;line-height:34px}
.program{position:absolute;font-family:"Source Sans 3",sans-serif;font-size:8.6px;line-height:10.6px;color:var(--text-dark)}
.program b{font-weight:600;font-size:16px;margin-right:3px}
.col-a{left:28px;width:235px}
.col-b{left:286px;width:218px}
.front-name{position:absolute;left:29px;top:522px;font-family:"Oswald",sans-serif;font-weight:600;font-size:19px;color:var(--ink);letter-spacing:1px}
.location{position:absolute;left:42px;top:664px;color:var(--paper);font-family:"Source Sans 3",sans-serif}
.location h3{font-weight:400;font-size:15px;line-height:18px}
.location p{font-weight:600;font-size:10.5px;line-height:13.5px}
.location .web{font-size:14px;line-height:18px;margin-top:1px}

/* Back page */
.back{position:absolute;left:610px;top:77px;width:524px;height:743px;overflow:hidden;background:var(--paper)}
.sheet{position:absolute;left:0;top:0;width:743px;height:524px;transform-origin:0 0;transform:translate(524px,0) rotate(90deg)}
.edge{position:absolute;left:0;top:0;width:743px;height:14px;background:var(--ink)}
.sheet-name{position:absolute;left:40px;top:42px;font-family:"Oswald",sans-serif;font-weight:600;font-size:17px;color:var(--ink);letter-spacing:.5px}
.sheet-title{position:absolute;left:243px;top:22px;font-family:"Anton",sans-serif;font-size:60px;line-height:66px;color:var(--ink);letter-spacing:1px}
.footer-band{position:absolute;left:0;top:466px;width:743px;height:58px;background:var(--ink);color:var(--paper);font-family:"Source Sans 3",sans-serif;padding-left:34px}
.footer-band .addr{font-size:12.5px;font-weight:600;margin-top:9px;line-height:15px}
.footer-band .web{font-size:16px;font-weight:700;letter-spacing:.6px;line-height:20px;margin-top:3px}

.day{position:absolute;width:228px;height:173px;font-family:"Roboto Condensed",sans-serif;font-size:6px}
.day h4{height:18px;background:var(--grey-bar);color:var(--paper);font-weight:700;font-size:8px;line-height:18px;padding-left:6px;letter-spacing:.3px}
.slot{display:grid;grid-template-columns:24px 66px 66px 1fr;height:17.2px;line-height:17.2px}
.slot span{padding-left:3px;white-space:nowrap;overflow:hidden}
.slot .t{color:var(--paper);font-weight:700;padding-left:4px}
.c1 .t{background:var(--blue)}    .c1{background:var(--blue-t)}
.c2 .t{background:var(--violet)}  .c2{background:var(--violet-t)}
.c3 .t{background:var(--magenta)} .c3{background:var(--magenta-t)}
.c4 .t{background:var(--amber)}   .c4{background:var(--amber-t)}
.c5 .t{background:var(--violet)}  .c5{background:var(--violet-t)}
.c6 .t{background:var(--pink)}    .c6{background:var(--pink-t)}
.c7 .t{background:var(--ink)}     .c7{background:var(--black-t)}
.c8 .t{background:var(--orange)}  .c8{background:var(--orange-t)}
.slot span:nth-child(3){background:rgba(255,255,255,.35)}
.slot span:nth-child(4){background:rgba(255,255,255,.6)}
.r1{top:97px}.r2{top:278px}
.k1{left:23px}.k2{left:259px}.k3{left:494px}
</style>
</head>
<body>
<div class="canvas">

  <section class="front">
    <svg class="front-bg" width="526" height="743" viewBox="0 0 526 743" aria-hidden="true">
      <defs>
        <linearGradient id="bodyShade" x1="0" x2="1" y1="0" y2="0">
          <stop offset="0" stop-color="#c4c4c4"/>
          <stop offset=".45" stop-color="#ffffff"/>
          <stop offset="1" stop-color="#bdbdbd"/>
        </linearGradient>
      </defs>
      <rect width="526" height="743" fill="url(#bodyShade)"/>
      <path d="M0 0H526V186C470 196 420 192 360 178C250 152 120 150 0 196Z" fill="#8e8e8e"/>
      <path d="M0 0H526V176C470 186 420 182 360 168C250 142 120 140 0 184Z" fill="#111111"/>
      <path d="M0 618C140 596 260 628 360 684C430 718 480 706 526 676V690C480 722 430 734 360 700C260 644 140 612 0 632Z" fill="#8e8e8e"/>
      <path d="M0 632C140 612 260 644 360 700C430 734 480 722 526 690V743H0Z" fill="#111111"/>
      <g role="img" aria-label="Circular photo of a boxer training on pads">
        <circle cx="338" cy="467" r="52" fill="#9a9a9a"/>
        <circle cx="338" cy="467" r="46" fill="#6b5a55"/>
      </g>
      <g role="img" aria-label="Circular photo of a member lifting a kettlebell">
        <circle cx="254" cy="511" r="54" fill="#9a9a9a"/>
        <circle cx="254" cy="511" r="48" fill="#3d4a45"/>
      </g>
      <g role="img" aria-label="Circular photo of group kettlebell training">
        <circle cx="290" cy="599" r="65" fill="#9a9a9a"/>
        <circle cx="290" cy="599" r="58" fill="#3f4a3c"/>
      </g>
      <g role="img" aria-label="Circular photo of a woman training with battle ropes">
        <circle cx="414" cy="611" r="106" fill="#9a9a9a"/>
        <circle cx="414" cy="611" r="99" fill="#4e5652"/>
      </g>
    </svg>

    <h1 class="headline">HARBOURLINE FORGE GYM IS A FUN COMMUNITY OF HUMBLE PEOPLE.</h1>
    <p class="tagline">Our goal is to help guide you towards a fitter, healthier lifestyle!</p>

    <h2 class="section-title">Our Programs</h2>

    <p class="program col-a" style="top:224px"><b>HIIT</b>High intensity interval training is 30-45 minutes of fat burning fun. The class is a mix of cardio, bodyweight and some resistance movements.</p>
    <p class="program col-a" style="top:276px"><b>Conditioning</b>A full hour of strength, cardio and bodyweight training to get you in tip top shape. Expect a mix of barbells, kettlebells, rowing machines, bikes and other training methods.</p>
    <p class="program col-a" style="top:336px"><b>QMP</b>This is our big Friday session to set you up for the weekend. 90 minutes of hard training that is done with a team emphasis. From heavy lifting to cardio triathlons, this class has it all but not for the faint hearted.</p>
    <p class="program col-a" style="top:397px"><b>Muay Thai</b>Commonly known as the science of 8 limbs you will learn how to punch, kick, knee and elbow. Thailands national sport is a great way to get your fitness kick. We train the complete beginner all the way to international fighters so you are in great hands.</p>

    <p class="program col-b" style="top:224px"><b>Kids Muay Thai</b>Our junior program starts from age 6 onwards. Muay Thai is a great way for kids to get active and fit while learning new skills. Training in martial arts also teaches self discipline and socialisation skills.</p>
    <p class="program col-b" style="top:296px"><b>Yoga</b>A combination of physical and mental practises that will leave you focused and refreshed for whatever the week throws at you. We always recommend our yoga classes as a great way to balance the high intensity training we offer.</p>
    <p class="program col-b" style="top:368px"><b>Q-Move</b>Strength training with a little bit of conditioning. We regularly update the program and re test lifts to ensure you are making progress and getting stronger.</p>

    <div class="front-name">HARBOURLINE FORGE GYM</div>

    <div class="location">
      <h3>OUR LOCATION:</h3>
      <p>Unit 27C, 214 Caskin Street Wester Holm, Glasgow G72LT</p>
      <p>Ph: 07392615084 | E: info@harbourlineforgegym.com</p>
      <p class="web">www.harbourlineforgegym.com</p>
    </div>
  </section>

  <section class="back">
    <div class="sheet">
      <div class="edge"></div>
      <div class="sheet-name">HARBOURLINE FORGE GYM</div>
      <h2 class="sheet-title">OUR TIMETABLE</h2>

      <div class="day r1 k1"><h4>MONDAY, 12 FEBRUARY 2018</h4>
        <div class="slot c1"><span class="t">07:00</span><span>Conditioning</span><span>Harbourline Forge Gym</span><span></span></div>
        <div class="slot c2"><span class="t">08:00</span><span>Open Gym</span><span>Harbourline Forge Gym</span><span></span></div>
        <div class="slot c3"><span class="t">10:00</span><span>Q-Move</span><span>Harbourline Forge Gym</span><span></span></div>
        <div class="slot c4"><span class="t">12:10</span><span>Lunchtime HIIT</span><span>Harbourline Forge Gym</span><span></span></div>
        <div class="slot c5"><span class="t">16:00</span><span>Open Gym</span><span>Harbourline Forge Gym</span><span></span></div>
        <div class="slot c6"><span class="t">17:00</span><span>Q-Move</span><span>Harbourline Forge Gym</span><span>(17 spots left)</span></div>
        <div class="slot c7"><span class="t">18:00</span><span>Fundamentals</span><span>Harbourline Forge Gym</span><span></span></div>
        <div class="slot c8"><span class="t">18:00</span><span>Muay Thai Foundations</span><span>Harbourline Forge Gym</span><span></span></div>
        <div class="slot c8"><span class="t">19:00</span><span>Strength and Conditioning</span><span>Harbourline Forge Gym</span><span></span></div>
      </div>

      <div class="day r1 k2"><h4>TUESDAY, 13 FEBRUARY 2018</h4>
        <div class="slot c1"><span class="t">07:00</span><span>Conditioning</span><span>Harbourline Forge Gym</span><span></span></div>
        <div class="slot c2"><span class="t">08:00</span><span>Open Gym</span><span>Harbourline Forge Gym</span><span></span></div>
        <div class="slot c3"><span class="t">10:00</span><span>Q-Move</span><span>Harbourline Forge Gym</span><span></span></div>
        <div class="slot c4"><span class="t">12:10</span><span>Lunchtime HIIT</span><span>Harbourline Forge Gym</span><span></span></div>
        <div class="slot c5"><span class="t">16:00</span><span>Open Gym</span><span>Harbourline Forge Gym</span><span></span></div>
        <div class="slot c6"><span class="t">17:00</span><span>Q-Move</span><span>Harbourline Forge Gym</span><span>(17 spots left)</span></div>
        <div class="slot c7"><span class="t">18:00</span><span>Fundamentals</span><span>Harbourline Forge Gym</span><span></span></div>
        <div class="slot c8"><span class="t">18:00</span><span>Muay Thai Foundations</span><span>Harbourline Forge Gym</span><span></span></div>
        <div class="slot c8"><span class="t">19:00</span><span>Strength and Conditioning</span><span>Harbourline Forge Gym</span><span></span></div>
      </div>

      <div class="day r1 k3"><h4>WEDNESDAY, 14 FEBRUARY 2018</h4>
        <div class="slot c1"><span class="t">07:00</span><span>Conditioning</span><span>Harbourline Forge Gym</span><span></span></div>
        <div class="slot c2"><span class="t">08:00</span><span>Open Gym</span><span>Harbourline Forge Gym</span><span></span></div>
        <div class="slot c3"><span class="t">10:00</span><span>Q-Move</span><span>Harbourline Forge Gym</span><span></span></div>
        <div class="slot c4"><span class="t">12:10</span><span>Lunchtime HIIT</span><span>Harbourline Forge Gym</span><span></span></div>
        <div class="slot c5"><span class="t">16:00</span><span>Open Gym</span><span>Harbourline Forge Gym</span><span></span></div>
        <div class="slot c6"><span class="t">17:00</span><span>Q-Move</span><span>Harbourline Forge Gym</span><span>(17 spots left)</span></div>
        <div class="slot c7"><span class="t">18:00</span><span>Fundamentals</span><span>Harbourline Forge Gym</span><span></span></div>
        <div class="slot c8"><span class="t">18:00</span><span>Muay Thai Foundations</span><span>Harbourline Forge Gym</span><span></span></div>
        <div class="slot c8"><span class="t">19:00</span><span>Strength and Conditioning</span><span>Harbourline Forge Gym</span><span></span></div>
      </div>

      <div class="day r2 k1"><h4>THURSDAY, 15 FEBRUARY 2018</h4>
        <div class="slot c1"><span class="t">07:00</span><span>Conditioning</span><span>Harbourline Forge Gym</span><span></span></div>
        <div class="slot c2"><span class="t">08:00</span><span>Open Gym</span><span>Harbourline Forge Gym</span><span></span></div>
        <div class="slot c3"><span class="t">10:00</span><span>Q-Move</span><span>Harbourline Forge Gym</span><span></span></div>
        <div class="slot c4"><span class="t">12:10</span><span>Lunchtime HIIT</span><span>Harbourline Forge Gym</span><span></span></div>
        <div class="slot c5"><span class="t">16:00</span><span>Open Gym</span><span>Harbourline Forge Gym</span><span></span></div>
        <div class="slot c6"><span class="t">17:00</span><span>Q-Move</span><span>Harbourline Forge Gym</span><span>(17 spots left)</span></div>
        <div class="slot c7"><span class="t">18:00</span><span>Fundamentals</span><span>Harbourline Forge Gym</span><span></span></div>
        <div class="slot c8"><span class="t">18:00</span><span>Muay Thai Foundations</span><span>Harbourline Forge Gym</span><span></span></div>
        <div class="slot c8"><span class="t">19:00</span><span>Strength and Conditioning</span><span>Harbourline Forge Gym</span><span></span></div>
      </div>

      <div class="day r2 k2"><h4>FRIDAY, 16 FEBRUARY 2018</h4>
        <div class="slot c1"><span class="t">07:00</span><span>Conditioning</span><span>Harbourline Forge Gym</span><span></span></div>
        <div class="slot c2"><span class="t">08:00</span><span>Open Gym</span><span>Harbourline Forge Gym</span><span></span></div>
        <div class="slot c3"><span class="t">10:00</span><span>Q-Move</span><span>Harbourline Forge Gym</span><span></span></div>
        <div class="slot c4"><span class="t">12:10</span><span>Lunchtime HIIT</span><span>Harbourline Forge Gym</span><span></span></div>
        <div class="slot c5"><span class="t">16:00</span><span>Open Gym</span><span>Harbourline Forge Gym</span><span></span></div>
        <div class="slot c6"><span class="t">17:00</span><span>Q-Move</span><span>Harbourline Forge Gym</span><span>(17 spots left)</span></div>
        <div class="slot c7"><span class="t">18:00</span><span>Fundamentals</span><span>Harbourline Forge Gym</span><span></span></div>
        <div class="slot c8"><span class="t">18:00</span><span>Muay Thai Foundations</span><span>Harbourline Forge Gym</span><span></span></div>
        <div class="slot c8"><span class="t">19:00</span><span>Strength and Conditioning</span><span>Harbourline Forge Gym</span><span></span></div>
      </div>

      <div class="day r2 k3"><h4>SATURDAY, 17 FEBRUARY 2018</h4>
        <div class="slot c1"><span class="t">07:00</span><span>Conditioning</span><span>Harbourline Forge Gym</span><span></span></div>
        <div class="slot c2"><span class="t">08:00</span><span>Open Gym</span><span>Harbourline Forge Gym</span><span></span></div>
        <div class="slot c3"><span class="t">10:00</span><span>Q-Move</span><span>Harbourline Forge Gym</span><span></span></div>
        <div class="slot c4"><span class="t">12:10</span><span>Lunchtime HIIT</span><span>Harbourline Forge Gym</span><span></span></div>
        <div class="slot c5"><span class="t">16:00</span><span>Open Gym</span><span>Harbourline Forge Gym</span><span></span></div>
        <div class="slot c6"><span class="t">17:00</span><span>Q-Move</span><span>Harbourline Forge Gym</span><span>(17 spots left)</span></div>
        <div class="slot c7"><span class="t">18:00</span><span>Fundamentals</span><span>Harbourline Forge Gym</span><span></span></div>
        <div class="slot c8"><span class="t">18:00</span><span>Muay Thai Foundations</span><span>Harbourline Forge Gym</span><span></span></div>
        <div class="slot c8"><span class="t">19:00</span><span>Strength and Conditioning</span><span>Harbourline Forge Gym</span><span></span></div>
      </div>

      <div class="footer-band">
        <p class="addr">Unit 27C, 214 Caskin Street Wester Holm, Glasgow G72LT | Ph: 07392615084 | E: info@harbourlineforgegym.com</p>
        <p class="web">WWW.HARBOURLINEFORGEGYM.COM</p>
      </div>
    </div>
  </section>

</div>
</body>
</html>
```